Full Page Magazine Ad for Law Firm

Full Page Magazine Ad

The project is to design a full page ad to be place in Cannabis Harvest Quarterly magazine in the November 2017 edition.

Purpose of the ad is to promote Copperfield Ridge Law Group and not Martin Osgood from mo LAW ad.

About 20% of Copperfield Ridge Law Group’s current practice is marijuana related and it is looking grow that by illustrating in the ad that mo LAW is joining the firm.

Copperfield Ridge Law Group offers services in
• Tax Law
• Securities & Finance
• Business & Corporations
• Business Structuring
• Investments Funds & Management
• Rest Estate
• Outside General Counsel

mo LAW has offered services in:

• Marijuana regulation and compliance
• Buying and selling marijuana businesses
• Business & Corporations

Color palate should match Copperfield Ridge Law Group logo (blue) color with gray, black, white.

DO NOT want marijuana leaf images.
DO NOT include picture of Martin Osgood from mo LAW ad.

Documents provided:
Copperfield Ridge Law Group logo
Past mo LAW ad in magazine
Examples of competitor ads in same publication
Magazine spec sheet

Target Market(s)

The target of the ad is owners of larger marijuana retail stores and marijuana production/processing operations that need legal services.

Industry/Entity Type

Law Firm

Font styles to use
Other font styles liked:
• Should fit with CRLG logo.

Colors
3276b5

Requirements
Must have
• Copperfield Ridge Law Group is the Primary focus
• Use Copperfield Ridge Law Group address / contact information
• Ad must make clear that Copperfield Ridge Law Group is a Law Firm offering legal services to businesses.
Should not have
• DO NOT want marijuana leaf images.
• DO NOT include picture of Martin Osgood from mo LAW ad

```html
<!DOCTYPE html>
<html lang="en">
<head>
<meta charset="utf-8">
<title>Copperfield Ridge Law Group – Full Page Ad</title>
<link rel="stylesheet" href="https://fonts.googleapis.com/css2?family=Open+Sans:wght@300;400;600&display=swap">
<style>
  :root {
    --backdrop: #d3d4d6;
    --paper: #ffffff;
    --brand-blue: #3276b5;
    --accent-light: #cfe9f8;
    --marker-blue: #5580aa;
    --ink: #3a3a3a;
    --white: #ffffff;
  }
  html, body {
    margin: 0;
    padding: 0;
    width: 955px;
    height: 1200px;
    overflow: hidden;
    background: var(--backdrop);
    font-family: "Open Sans", Arial, sans-serif;
  }
  .ad-page {
    position: absolute;
    left: 90px;
    top: 52px;
    width: 791px;
    height: 1044px;
    background: var(--paper);
    box-shadow: 4px 6px 8px rgba(0,0,0,0.35);
    overflow: hidden;
  }
  .ad-shapes { position: absolute; inset: 0; }
  .headline {
    position: absolute;
    left: 60px;
    top: 76px;
    margin: 0;
    width: 390px;
    color: var(--white);
    font-weight: 300;
    font-size: 29px;
    line-height: 39px;
    letter-spacing: 0.3px;
  }
  .firm-name {
    position: absolute;
    left: 601px;
    top: 100px;
    width: 161px;
    display: flex;
    align-items: flex-start;
    gap: 10px;
    margin: 0;
    color: var(--ink);
    font-weight: 400;
    font-size: 19px;
    line-height: 25px;
  }
  .firm-name .marker {
    flex: 0 0 18px;
    height: 18px;
    margin-top: 4px;
    background: var(--marker-blue);
  }
  .team-photo {
    position: absolute;
    left: 0;
    top: 260px;
    width: 791px;
    height: 282px;
    background: linear-gradient(180deg, #e4e8ee 0%, #cfd7e2 55%, #9fb0c4 100%);
  }
  .services {
    position: absolute;
    left: 45px;
    color: var(--white);
    font-weight: 300;
  }
  .services-intro {
    margin: 0;
    font-size: 18px;
    line-height: 24px;
  }
  .service-list {
    list-style: none;
    margin: 4px 0 0;
    padding: 0;
    font-size: 16.5px;
    line-height: 26.6px;
  }
  .service-list li::before {
    content: "•";
    display: inline-block;
    width: 14px;
    padding-left: 4px;
    font-weight: 400;
  }
  .firm-services { top: 600px; }
  .partner-services { top: 870px; }
  .partner-name {
    margin: 0 0 4px;
    font-size: 35px;
    line-height: 44px;
    font-weight: 400;
  }
  .contact {
    position: absolute;
    right: 29px;
    top: 862px;
    margin: 0;
    text-align: right;
    font-style: normal;
    color: var(--ink);
    font-size: 17.5px;
    line-height: 23.5px;
  }
</style>
</head>
<body>
  <main class="ad-page">
    <svg class="ad-shapes" width="791" height="1044" viewBox="0 0 791 1044" aria-hidden="true">
      <defs>
        <linearGradient id="top-band" x1="0" y1="0" x2="1" y2="1">
          <stop offset="0" stop-color="#2a78c6"/>
          <stop offset="0.5" stop-color="#1a8fd6"/>
          <stop offset="1" stop-color="#2b6fc0"/>
        </linearGradient>
      </defs>
      <path d="M410 0 H432 Q492 120 508 260 H488 Q470 120 410 0 Z" fill="var(--accent-light)"/>
      <path d="M0 0 H410 Q470 120 488 260 H0 Z" fill="url(#top-band)"/>
      <path d="M562 542 H582 Q580 820 432 1044 H410 Q560 820 562 542 Z" fill="var(--accent-light)"/>
      <path d="M0 542 H562 Q560 820 410 1044 H0 Z" fill="var(--brand-blue)"/>
    </svg>

    <h1 class="headline">Copperfield Ridge Law Group offering legal services to businesses.</h1>

    <p class="firm-name"><span class="marker" aria-hidden="true"></span><span>Copperfield Ridge Law Group</span></p>

    <div class="team-photo" role="img" aria-label="Photo of business professionals talking in a bright office with large windows"></div>

    <section class="services firm-services">
      <p class="services-intro">Copperfield Ridge Law Group offers services in:</p>
      <ul class="service-list">
        <li>Tax Law</li>
        <li>Securities &amp; Finance</li>
        <li>Business &amp; Corporations</li>
        <li>Business Structuring</li>
        <li>Investments Funds &amp; Management</li>
        <li>Rest Estate</li>
        <li>Outside General Counsel</li>
      </ul>
    </section>

    <section class="services partner-services">
      <h2 class="partner-name">mo LAW</h2>
      <p class="services-intro">mo LAW has offered services in:</p>
      <ul class="service-list">
        <li>Marijuana regulation and compliance</li>
        <li>Buying and selling marijuana businesses</li>
        <li>Business &amp; Corporations</li>
      </ul>
    </section>

    <address class="contact">
      1240 Harbor Ridge Avenue<br>
      Suite 1900<br>
      Seattle, WA&nbsp; 98101<br>
      206.555.0140<br>
      206.555.0141 (fax)<br>
      www.copperfieldridgelaw.com
    </address>
  </main>
</body>
</html>
```